Modern Corporate Brochure For Australian Real Estate Agency

We need a corporate 10 page A4 brochure for a Australian Real Estate agency with information for our clients and referral partners.

Main colour scheme: #238b53

Examples of designs:
https://quillmarsh.net/item/8-page-corporate-business-brochure/5827314

https://quillmarsh.net/item/brochure/27461983

https://quillmarsh.net/item/the-company-profile/38150726

https://quillmarsh.net/item/brochure-pack-a4trifold-leafletbusiness-card/736182

Target Market(s)

Professional Australians

Industry/Entity Type

Real Estate

Font styles to use
Sans Serif

Requirements
Must have
• Use of multiple greens from the logo

```html
<!DOCTYPE html>
<html lang="en">
<head>
<meta charset="utf-8">
<title>Kestrel Property Group – Brochure Covers</title>
<link href="https://fonts.googleapis.com/css2?family=Montserrat:wght@300;700;800&family=Open+Sans:wght@400;700&display=swap" rel="stylesheet">
<style>
  :root{
    --green:#238b53;
    --green-bright:#2fa462;
    --green-dark:#0f4a2c;
    --green-deep:#0a2f1c;
    --ink:#2b2b2b;
    --text:#444;
    --paper:#ffffff;
    --backdrop:#7a8b98;
  }
  *{box-sizing:border-box;margin:0;padding:0}
  html,body{width:1200px;height:824px;overflow:hidden}
  body{background:var(--backdrop);font-family:"Open Sans",Arial,sans-serif;color:var(--text)}
  .spread{position:absolute;left:48px;top:22px;width:1104px;height:780px;display:flex;box-shadow:0 10px 30px rgba(0,0,0,.25)}
  .page{position:relative;width:552px;height:780px;background:var(--paper);overflow:hidden}
  .page svg.art{position:absolute;inset:0;width:552px;height:780px}

  /* back cover */
  .sales{position:absolute;left:48px;top:70px;width:300px}
  .sales h2{font-family:"Montserrat",Arial,sans-serif;font-weight:700;font-size:20px;color:var(--ink);margin-bottom:10px}
  .sales p{font-size:12px;line-height:1.5}
  .contact{position:absolute;left:48px;top:612px}
  .contact h3{font-family:"Montserrat",Arial,sans-serif;font-weight:800;font-size:20px;color:var(--green);margin-bottom:8px}
  .contact ul{list-style:none;font-size:13px;color:var(--ink)}
  .contact li{display:flex;align-items:flex-start;gap:10px;line-height:1.35;margin-bottom:3px}
  .contact li svg{flex:none;margin-top:3px}
  .contact b{font-weight:700}
  .rule-bottom{position:absolute;left:48px;right:60px;bottom:20px;height:5px;background:var(--green)}

  /* front cover */
  .brand{position:absolute;right:48px;top:58px;display:flex;align-items:center;gap:10px}
  .brand-square{width:22px;height:22px;background:var(--green)}
  .brand-name{font-family:"Montserrat",Arial,sans-serif;font-weight:700;font-size:19px;color:var(--ink);letter-spacing:.5px}
  .headline{position:absolute;right:44px;top:258px;text-align:right;color:#fff;font-family:"Montserrat",Arial,sans-serif;line-height:1}
  .headline .light{display:block;font-weight:300;font-size:46px}
  .headline .bold{display:block;font-weight:800;font-size:48px;margin-top:6px}
  .tab{position:absolute;left:0;top:560px;width:12px;height:86px;background:var(--green-bright)}
  .management{position:absolute;left:60px;top:555px;width:440px}
  .management h2{font-family:"Montserrat",Arial,sans-serif;font-weight:700;font-size:20px;color:var(--ink);margin-bottom:8px}
  .management p{font-size:12px;line-height:1.5;text-align:justify}
  .site{position:absolute;left:0;right:0;top:712px;text-align:center;font-size:16px;color:var(--ink)}
  .site b{color:var(--green);font-weight:700}
</style>
</head>
<body>
<main class="spread">

  <section class="page back-cover">
    <svg class="art" viewBox="0 0 552 780">
      <defs>
        <linearGradient id="cityBack" x1="0" y1="0" x2="0" y2="1">
          <stop offset="0" stop-color="#1d6a42"/>
          <stop offset=".6" stop-color="#0f3f26"/>
          <stop offset="1" stop-color="#1f7a49"/>
        </linearGradient>
      </defs>
      <polygon points="552,0 552,500 0,600 0,330 300,330" fill="url(#cityBack)" role="img" aria-label="Night photograph of a city skyline by the river, tinted green"/>
      <polygon points="552,0 552,260 300,330" fill="var(--green-dark)" opacity=".55"/>
    </svg>

    <div class="sales">
      <h2>Brisbane Property Sales</h2>
      <p>When selling your property it is important to select an agent who is a part of an agency with a great culture and proven results in selling property regardless of market conditions.</p>
    </div>

    <div class="contact">
      <h3>Contact Us:</h3>
      <ul>
        <li><svg width="12" height="12" viewBox="0 0 12 12"><circle cx="6" cy="6" r="6" fill="#222"/><path d="M4 3.2l1 1.4-.6.7c.4.8 1 1.4 1.8 1.8l.7-.6 1.4 1-.6 1.2C5.8 8.4 3.6 6.2 3 4z" fill="#fff"/></svg><span>(07) 5550 1847</span></li>
        <li><svg width="12" height="12" viewBox="0 0 12 12"><circle cx="6" cy="6" r="6" fill="#222"/><circle cx="6" cy="6" r="3.6" fill="none" stroke="#fff" stroke-width=".8"/><path d="M2.4 6h7.2M6 2.4v7.2" stroke="#fff" stroke-width=".8"/></svg><span>www.<b>kestrelproperty</b>.com.au</span></li>
        <li><svg width="12" height="12" viewBox="0 0 12 12"><circle cx="6" cy="6" r="6" fill="#222"/><rect x="3" y="4" width="6" height="4.2" fill="#fff"/><path d="M3 4l3 2.3L9 4" fill="none" stroke="#222" stroke-width=".7"/></svg><span>info@<b>kestrelproperty</b>.com.au</span></li>
        <li><svg width="12" height="12" viewBox="0 0 12 12"><circle cx="6" cy="6" r="6" fill="#222"/><circle cx="6" cy="5.3" r="2.2" fill="#fff"/><circle cx="6" cy="5.3" r=".9" fill="#222"/></svg><span>58 Marlowe St, Riverton Heights<br>Brisbane 4006</span></li>
      </ul>
    </div>
    <div class="rule-bottom"></div>
  </section>

  <section class="page front-cover">
    <svg class="art" viewBox="0 0 552 780">
      <defs>
        <linearGradient id="cityFront" x1="0" y1="0" x2="1" y2="1">
          <stop offset="0" stop-color="#1f6e45"/>
          <stop offset=".55" stop-color="#0c3520"/>
          <stop offset="1" stop-color="#1c6f43"/>
        </linearGradient>
      </defs>
      <polygon points="0,0 200,230 552,180 552,370 250,470 0,400" fill="url(#cityFront)" role="img" aria-label="Night photograph of city towers reflected in the river, tinted green"/>
      <polygon points="0,0 200,230 0,300" fill="var(--green-dark)" opacity=".6"/>
    </svg>

    <div class="brand">
      <span class="brand-square"></span>
      <span class="brand-name">KESTREL PROPERTY GROUP</span>
    </div>

    <h1 class="headline"><span class="light">A Refreshing</span><span class="bold">Change</span></h1>

    <div class="tab"></div>
    <div class="management">
      <h2>Residential Property Management</h2>
      <p>It is common to find that within the overwhelming majority of real estate offices the property management department is the most under-resourced. It’s no wonder investors move from one agency to another in search of a decent property manager and agency to work with.</p>
    </div>

    <p class="site">www.<b>kestrelproperty</b>.com.au</p>
  </section>

</main>
</body>
</html>
```